We need a PowerPoint to outline what Modeling is about!

PowerPoint presentation to be shown to aspiring models. The students will be joining our 1-day workshop, and they will be taught the very basics of being a model.
What should be included in the slides:
• What is Modelling? - Description of Modelling, and what it takes to be a Model.
• Types of Models in the market - Catwalk Model / Photography Model / Events Model
• Expectations of a model - Professionalism, Punctuality, Confidence, etc etc.
• Practical (catwalk) tips: Posture
• Practical (catwalk) tips: How to do a simple catwalk
• Practical (photography) tips: How to bring out your best angles in photos
• Trainer Assessment of Students
Here are some definitions that we use. You may change the wording as you see fit, as long as the meaning is the same.
Modelling is to promote a product / brand / service in an advertisement, show, commercial or event.
Runway / Fashion Model – Walk the catwalk to promote clothing and accessories in a fashion show.
Most shows require the model to be tall and skinny. Model needs to strut with confidence and grace down the runway. Body shape more important than facial features.
Photography Model – Appear for Print Ads, Magazine Editorials, Posters, etc.
Height requirements are not as strict (or not present) as compared to Runway Model. Good features preferred, but not a must.
Video Model – Appear for TV commercials, Promotional Videos, etc.
Model needs to possess basic acting skills to promote the product, brand or service on video. Confidence and screen charisma more important than looks or body.
Events Model – Promote the product, brand or service during ‘live’ events and shows.
Model needs to be engaging and charismatic to ‘sell’ the product to customers.
A longer description can also be found here: http://www.brightlarkagency.sg/models/
Target Market(s)
Adults aged 18 - 40 who are interested to take up Modeling.
Industry/Entity Type
Events
Requirements
Must have
- Visually appealing! Does not have to be content heavy, but should deliver the message effectively.
Nice to have
- Pretty pictures.

```html
<!DOCTYPE html>
<html lang="en">
<head>
<meta charset="utf-8">
<title>Practical Photography Tips</title>
<link rel="stylesheet" href="https://fonts.googleapis.com/css2?family=Poiret+One&family=Source+Sans+3:wght@400;600&display=swap">
<style>
  :root {
    --slide-bg: #e5e5e5;
    --accent-pink: #ec1762;
    --ink: #1e1e1e;
    --block-black: #000000;
    --brand-dark: #3a3a3a;
    --art-light: #d4d4d4;
    --art-dark: #9a9a9a;
  }
  * { margin: 0; padding: 0; box-sizing: border-box; }
  html, body { width: 1200px; height: 900px; overflow: hidden; background: var(--slide-bg); }
  .slide {
    position: relative;
    width: 1200px;
    height: 900px;
    background: var(--slide-bg);
    overflow: hidden;
    font-family: "Source Sans 3", "Calibri", sans-serif;
    color: var(--ink);
  }
  .accent-bar {
    position: absolute; left: 0; top: 0;
    width: 690px; height: 38px;
    background: var(--accent-pink);
  }
  .slide-title {
    position: absolute; left: 0; top: 82px; width: 1200px;
    text-align: center;
    font-family: "Poiret One", "Federo", sans-serif;
    font-weight: 400;
    font-size: 64px;
    letter-spacing: 6px;
    color: var(--ink);
    -webkit-text-stroke: 1.6px var(--ink);
    text-transform: uppercase;
  }
  .corner-block {
    position: absolute; left: 1090px; top: 243px;
    width: 110px; height: 138px;
    background: var(--block-black);
  }
  .tips-list {
    position: absolute; left: 160px; top: 252px;
    list-style: none;
  }
  .tips-list li {
    display: flex; align-items: center;
    height: 45.6px;
    font-size: 29px;
    line-height: 1;
  }
  .tip-marker {
    width: 58px; height: 16px;
    margin-right: 47px;
    background: linear-gradient(100deg, #6a6a6a, #2a2a2a 60%, #555);
    border-radius: 2px 8px 8px 2px;
    transform: skewX(-18deg);
  }
  .studio-art {
    position: absolute; left: 700px; top: 430px;
    width: 500px; height: 470px;
    background: linear-gradient(90deg, var(--art-light) 0%, var(--art-dark) 45%, var(--art-light) 60%, #2b2b2b 100%);
    opacity: 0.55;
  }
  .brand {
    position: absolute; left: 32px; top: 835px;
    display: flex; align-items: center; gap: 10px;
  }
  .brand-square { width: 26px; height: 26px; background: var(--brand-dark); }
  .brand-name {
    font-size: 20px; font-weight: 600;
    color: var(--brand-dark);
  }
</style>
</head>
<body>
  <main class="slide">
    <div class="accent-bar"></div>
    <h1 class="slide-title">Practical Photography Tips</h1>
    <div class="corner-block"></div>

    <ul class="tips-list">
      <li><span class="tip-marker" role="img" aria-label="Brush stroke bullet"></span>Clarify your skin.</li>
      <li><span class="tip-marker" role="img" aria-label="Brush stroke bullet"></span>Focus on what makes you unique.</li>
      <li><span class="tip-marker" role="img" aria-label="Brush stroke bullet"></span>Show your emotions.</li>
      <li><span class="tip-marker" role="img" aria-label="Brush stroke bullet"></span>Don’t look the camera straight on.</li>
      <li><span class="tip-marker" role="img" aria-label="Brush stroke bullet"></span>Adjust the angle of your face.</li>
      <li><span class="tip-marker" role="img" aria-label="Brush stroke bullet"></span>Work your assets.</li>
      <li><span class="tip-marker" role="img" aria-label="Brush stroke bullet"></span>Bend your joints.</li>
      <li><span class="tip-marker" role="img" aria-label="Brush stroke bullet"></span>Lean towards the camera.</li>
      <li><span class="tip-marker" role="img" aria-label="Brush stroke bullet"></span>Do what’s comfortable.</li>
      <li><span class="tip-marker" role="img" aria-label="Brush stroke bullet"></span>Find the right light source.</li>
      <li><span class="tip-marker" role="img" aria-label="Brush stroke bullet"></span>Choose a great location.</li>
    </ul>

    <div class="studio-art" role="img" aria-label="Illustration of a studio umbrella light on a stand beside a stylised fashion model in a striped top"></div>

    <div class="brand">
      <span class="brand-square"></span>
      <span class="brand-name">Bright Lark Agency</span>
    </div>
  </main>
</body>
</html>
```